Simple, clean boat charter Banners

We need a variety of banner designs for our charter boat company. We provide boat trips to marlow shoals, beaches and snorkeling. You can see our site www.velmarotrips.com to get a better idea of our image.

We need the banner to be clean, simple and pleasing to the eye. The following ad dimensions we need are:

300 x 250
336 x 280
728 x 90
300 x 600
320 x 100

I've included a range of photos and logos to pic from.

Ignore the logo in all the photos. If a portion of the logo in the photo is in the banner, down worry. I will proved photos with the logo removed for the winning designs.

Please include a phrase, such as the following:
- Private Boat Charters to Marlow Shoals
- Private Boat Charters in Grand Cayman

If you can think of fun witty phrases, feel free to try them out. We are very open to creative ideas!! For example:
- Come visit the stingrays with us!
- Have you ever kissed a stingray?

Target Market(s)

Up-scale 30-50 year olds residing in North America

Industry/Entity Type

Tourism

Colors
3176b5
0655a3
85cae6
33a6d7
0592cd
cee9f5

Requirements
Nice to have
• Clean, Simple, Modern

```html
<!DOCTYPE html>
<html lang="en">
<head>
<meta charset="utf-8">
<title>Velmaro Trips – Banner Set</title>
<link rel="stylesheet" href="https://fonts.googleapis.com/css2?family=PT+Serif:ital,wght@0,700;1,700&family=Source+Sans+3:wght@400&display=swap">
<style>
  :root {
    --sheet: #e7e8e9;
    --label: #8a8b8d;
    --navy: #1d3f8a;
    --deep: #0655a3;
    --sky: #85cae6;
    --aqua: #33a6d7;
    --sea: #0592cd;
    --foam: #cee9f5;
    --white: #ffffff;
    --url: #4a4a4a;
    --cue: rgba(255,255,255,.55);
    --serif: "PT Serif", Georgia, serif;
    --sans: "Source Sans 3", Arial, sans-serif;
  }
  * { margin: 0; padding: 0; box-sizing: border-box; }
  html, body { width: 1028px; height: 1200px; overflow: hidden; background: var(--sheet); }
  .sheet { position: relative; width: 1028px; height: 1200px; }

  .size-label { position: absolute; font: 400 13px var(--sans); color: var(--label); }

  .banner {
    position: absolute; overflow: hidden; background: var(--white);
    box-shadow: 0 9px 6px -5px rgba(0,0,0,.45);
  }
  .photo {
    position: absolute; inset: 0;
    background:
      radial-gradient(ellipse 60% 40% at 50% 95%, rgba(206,233,245,.75), transparent 70%),
      radial-gradient(ellipse 45% 30% at 55% 55%, rgba(5,146,205,.55), transparent 75%),
      linear-gradient(180deg, #1f7fc2 0%, #33a6d7 40%, #6cc0e0 75%, #a6d9ea 100%);
  }
  .photo-cue {
    position: absolute; border: 1.5px dashed var(--cue); border-radius: 4px;
    display: flex; align-items: center; justify-content: center;
  }
  .photo-cue svg { width: 34px; height: 28px; }
  .shapes { position: absolute; inset: 0; width: 100%; height: 100%; }

  .headline {
    position: absolute; font: italic 700 19px/1.28 var(--serif);
    color: var(--white); text-shadow: 0 1px 3px rgba(0,0,0,.45);
    text-align: center; white-space: nowrap;
  }
  .headline.on-white { color: var(--navy); text-shadow: none; }
  .url { position: absolute; font: 400 12px var(--sans); color: var(--url); white-space: nowrap; }
  .url.on-photo { color: var(--white); }
  .brand {
    position: absolute; font: 700 18px var(--serif); color: var(--deep);
    letter-spacing: 2px; text-transform: uppercase; white-space: nowrap; text-align: center;
  }
</style>
</head>
<body>
<div class="sheet">

  <svg width="0" height="0" style="position:absolute">
    <symbol id="picture-icon" viewBox="0 0 34 28">
      <rect x="1" y="1" width="32" height="26" rx="2" fill="none" stroke="rgba(255,255,255,.7)" stroke-width="2"/>
      <circle cx="10" cy="9" r="3" fill="rgba(255,255,255,.7)"/>
      <path d="M3 24 L13 14 L19 20 L24 15 L31 24Z" fill="rgba(255,255,255,.7)"/>
    </symbol>
  </svg>

  <!-- 728x90 -->
  <span class="size-label" style="left:86px;top:98px">728x90</span>
  <div class="banner" style="left:86px;top:119px;width:874px;height:108px">
    <div class="photo" role="img" aria-label="Photo: family snorkeling underwater in clear blue water">
      <div class="photo-cue" style="left:200px;top:8px;width:440px;height:92px"><svg aria-hidden="true"><use href="#picture-icon"/></svg></div>
    </div>
    <svg class="shapes" viewBox="0 0 874 108" preserveAspectRatio="none">
      <path d="M708 0 Q612 54 698 108 L874 108 L874 0Z" fill="var(--sky)"/>
      <path d="M720 0 Q626 54 710 108 L874 108 L874 0Z" fill="var(--navy)"/>
      <path d="M738 0 Q648 54 728 108 L874 108 L874 0Z" fill="var(--white)"/>
    </svg>
    <div class="headline" style="left:6px;top:30px;width:170px">Come visit the<br>stingrays with us!</div>
    <span class="url on-photo" style="left:27px;top:80px;font-size:11px">www.velmarotrips.com</span>
    <span class="brand" style="left:700px;top:40px;width:174px;font-size:18px">Velmaro Trips</span>
  </div>

  <!-- 320x100 -->
  <span class="size-label" style="left:86px;top:259px">320 x 100</span>
  <div class="banner" style="left:86px;top:278px;width:385px;height:121px">
    <div class="photo" role="img" aria-label="Photo: family snorkeling underwater together">
      <div class="photo-cue" style="left:10px;top:10px;width:200px;height:101px"><svg aria-hidden="true"><use href="#picture-icon"/></svg></div>
    </div>
    <svg class="shapes" viewBox="0 0 385 121" preserveAspectRatio="none">
      <path d="M246 0 Q166 60 236 121 L385 121 L385 0Z" fill="var(--sky)"/>
      <path d="M254 0 Q178 60 246 121 L385 121 L385 0Z" fill="var(--navy)"/>
      <path d="M266 0 Q192 60 258 121 L385 121 L385 0Z" fill="var(--white)"/>
    </svg>
    <div class="headline on-white" style="left:237px;top:10px;width:150px;font-size:15px;line-height:1.2">Come visit the<br>stingrays with us!</div>
    <span class="brand" style="left:239px;top:70px;width:150px;font-size:13px">Velmaro Trips</span>
    <span class="url" style="left:250px;top:98px;font-size:11px">www.velmarotrips.com</span>
  </div>

  <!-- 300x250 -->
  <span class="size-label" style="left:86px;top:416px">300x250</span>
  <div class="banner" style="left:86px;top:435px;width:361px;height:300px">
    <div class="photo" role="img" aria-label="Photo: family snorkeling underwater with a stingray">
      <div class="photo-cue" style="left:40px;top:70px;width:280px;height:120px"><svg aria-hidden="true"><use href="#picture-icon"/></svg></div>
    </div>
    <svg class="shapes" viewBox="0 0 361 300" preserveAspectRatio="none">
      <path d="M0 212 C90 262 180 268 361 232 L361 300 L0 300Z" fill="var(--sky)"/>
      <path d="M0 198 C90 252 200 258 361 228 L361 300 L0 300Z" fill="var(--navy)"/>
      <path d="M0 232 C110 262 220 262 361 236 L361 300 L0 300Z" fill="var(--sky)"/>
      <path d="M0 256 C140 272 240 252 361 240 L361 300 L0 300Z" fill="var(--white)"/>
    </svg>
    <div class="headline" style="left:80px;top:14px;width:200px">Come visit the<br>stingrays with us!</div>
    <span class="brand" style="left:216px;top:260px;width:148px;font-size:14px">Velmaro Trips</span>
    <span class="url" style="left:13px;top:280px">www.velmarotrips.com</span>
  </div>

  <!-- 336x280 -->
  <span class="size-label" style="left:86px;top:743px">336x280</span>
  <div class="banner" style="left:86px;top:762px;width:404px;height:336px">
    <div class="photo" role="img" aria-label="Photo: family snorkeling underwater with a stingray">
      <div class="photo-cue" style="left:50px;top:80px;width:304px;height:132px"><svg aria-hidden="true"><use href="#picture-icon"/></svg></div>
    </div>
    <svg class="shapes" viewBox="0 0 404 336" preserveAspectRatio="none">
      <path d="M0 238 C100 292 200 300 404 260 L404 336 L0 336Z" fill="var(--sky)"/>
      <path d="M0 222 C100 282 224 288 404 255 L404 336 L0 336Z" fill="var(--navy)"/>
      <path d="M0 260 C124 294 246 292 404 264 L404 336 L0 336Z" fill="var(--sky)"/>
      <path d="M0 288 C156 306 268 282 404 268 L404 336 L0 336Z" fill="var(--white)"/>
    </svg>
    <div class="headline" style="left:92px;top:18px;width:220px;font-size:21px">Come visit the<br>stingrays with us!</div>
    <span class="brand" style="left:244px;top:293px;width:160px;font-size:15px">Velmaro Trips</span>
    <span class="url" style="left:14px;top:312px;font-size:13px">www.velmarotrips.com</span>
  </div>

  <!-- 300x600 -->
  <span class="size-label" style="left:600px;top:355px">300x600</span>
  <div class="banner" style="left:600px;top:375px;width:360px;height:720px">
    <div class="photo" role="img" aria-label="Photo: family snorkeling underwater in turquoise water">
      <div class="photo-cue" style="left:20px;top:150px;width:320px;height:300px"><svg aria-hidden="true" style="width:48px;height:40px"><use href="#picture-icon"/></svg></div>
    </div>
    <svg class="shapes" viewBox="0 0 360 720" preserveAspectRatio="none">
      <path d="M0 614 C120 636 240 600 360 596 L360 720 L0 720Z" fill="var(--navy)"/>
      <path d="M0 630 C120 646 240 612 360 606 L360 720 L0 720Z" fill="var(--sky)"/>
      <path d="M0 660 C130 650 250 616 360 610 L360 720 L0 720Z" fill="var(--white)"/>
    </svg>
    <div class="headline" style="left:20px;top:470px;width:320px;font-size:30px;line-height:1.25">Come visit the<br>stingrays with us!</div>
    <span class="brand" style="left:184px;top:664px;width:176px;font-size:18px">Velmaro Trips</span>
    <span class="url" style="left:18px;top:694px;font-size:13px">www.velmarotrips.com</span>
  </div>

</div>
</body>
</html>
```